Designs of screens for job search mobile app

Design the following screens:

1. Login
2. Job search results in tabs
3. Job details in cards format
4. Profile
5. Settings

Logo and references are provided. The app need to be playful, easy to use, different from traditional job search app like Workvane, ProLattice and others and targeted to Millennial users (age 18-30).

The main app reference is Piqto, in terms of the colorful and fun color and font scheme.

Target Market(s)

Millennial users (age 18-30).

Requirements
Must have
• A fun, playful feel

```html
<!DOCTYPE html>
<html lang="en">
<head>
<meta charset="utf-8">
<title>Roamjobs – Job Search App Screens</title>
<link rel="stylesheet" href="https://fonts.googleapis.com/css2?family=Open+Sans:wght@400;600;700&display=swap">
<style>
:root{
  --pink:#ef5a9d;
  --pink-deep:#e2438a;
  --cyan:#9ae6f4;
  --cyan-soft:#cdf4fb;
  --cyan-pale:#effcff;
  --ink:#2b2f33;
  --muted:#7b8790;
  --link:#2aa9d6;
  --board:#e2e2e2;
  --fb:#3b6fc4;
  --white:#ffffff;
}
*{box-sizing:border-box;margin:0;padding:0}
html,body{width:1200px;height:2202px;overflow:hidden;background:var(--white)}
body{font-family:"Open Sans",Arial,sans-serif;color:var(--ink);position:relative}
.board{position:absolute;left:61px;top:49px;width:1074px;height:2063px;
  background:linear-gradient(180deg,var(--cyan) 0,var(--cyan) 311px,var(--board) 311px,var(--board) 1790px,#f6bcd5 1880px,var(--pink) 2063px)}
.screen{position:absolute;display:flex;flex-direction:column;background:linear-gradient(180deg,var(--cyan-soft),var(--cyan-pale));
  box-shadow:0 4px 10px rgba(0,0,0,.25);overflow:hidden}
.status{flex:none;height:16px;display:flex;justify-content:space-between;align-items:center;padding:0 8px;font-size:7px;background:var(--white);color:var(--ink)}
.appbar{flex:none;height:28px;background:var(--pink);color:var(--white);font-weight:700;font-size:12px;display:flex;align-items:center;justify-content:center;position:relative;border-bottom:2px solid var(--pink-deep)}
.appbar .back{position:absolute;left:8px;top:8px;width:0;height:0;border-top:6px solid transparent;border-bottom:6px solid transparent;border-right:8px solid var(--white)}
.appbar .close{position:absolute;left:9px;top:5px;font-weight:400;font-size:14px}
.body{flex:1;min-height:0;position:relative;padding:8px;overflow:hidden}
.tabbar{flex:none;height:44px;background:var(--pink);display:flex;justify-content:space-around;align-items:center;padding:0 4px}
.tab{width:36px;height:34px;background:var(--white);border-radius:4px;display:flex;align-items:center;justify-content:center}
.tab svg{width:26px;height:24px}
.btn{background:var(--pink);color:var(--white);font-weight:700;font-size:9px;border-radius:3px;display:inline-flex;align-items:center;justify-content:center}
.card{background:var(--white);border-radius:4px;box-shadow:0 1px 2px rgba(0,0,0,.2)}
.wordmark{color:var(--ink);font-weight:700;letter-spacing:.2px}

/* login */
.login-splash{background:linear-gradient(180deg,var(--white) 0,#d7f6fc 45%,var(--cyan) 100%)}
.login-splash .center{flex:1;display:flex;flex-direction:column;align-items:center;justify-content:center;gap:14px}
.login-splash .wordmark{font-size:26px}
.connecting{color:var(--link);font-size:10px;font-weight:600}
.login-photo .brandbar{flex:none;height:26px;background:var(--white);display:flex;justify-content:center;align-items:center;border-bottom:1px solid #dfe8ea}
.login-photo .brandbar .wordmark{font-size:11px}
.photo{flex:1;position:relative}
.photo .overlay{position:absolute;left:0;right:0;bottom:18px;display:flex;flex-direction:column;align-items:center;gap:8px}
.caption{color:var(--white);font-size:9px;font-weight:600}
.dots{display:flex;gap:4px}
.dots i{width:4px;height:4px;border-radius:50%;background:rgba(255,255,255,.55)}
.dots i.on{background:var(--white)}
.fb-btn{width:150px;height:22px;background:var(--fb);color:var(--white);font-size:8px;border-radius:3px;display:flex;align-items:center;justify-content:center;gap:6px}
.fb-btn i{width:9px;height:9px;background:var(--white);border-radius:2px}

/* results */
.result{display:flex;gap:8px;align-items:center;padding:5px 7px;margin-bottom:5px;height:54px;position:relative}
.co-mark{width:24px;height:24px;border-radius:50%;flex:none}
.result h4{font-size:8px;font-weight:700}
.result p{font-size:7px;color:var(--muted);line-height:1.3}
.result .ago{position:absolute;right:7px;bottom:4px;font-size:6px;color:var(--muted)}

/* search form */
.field{height:22px;background:var(--white);border:1px solid #9fd8e6;border-radius:3px;display:flex;align-items:center;justify-content:space-between;font-size:7px;color:var(--link);font-weight:600;padding-left:8px;overflow:hidden}
.field .drop{width:20px;height:100%;background:var(--link);position:relative}
.field .drop::after{content:"";position:absolute;left:6px;top:8px;border-left:4px solid transparent;border-right:4px solid transparent;border-top:5px solid var(--white)}
.search-form{position:absolute;left:24px;right:24px;top:70px;display:flex;flex-direction:column;gap:18px}
.search-go{position:absolute;left:50%;top:248px;transform:translateX(-50%);width:72px;height:14px;background:var(--link);color:var(--white);font-size:7px;font-weight:700;border-radius:3px;display:flex;align-items:center;justify-content:center}

/* details */
.detail{padding:8px;height:100%;font-size:6.6px;line-height:1.45}
.detail .head{display:flex;gap:8px;align-items:center;position:relative;padding-bottom:8px;border-bottom:1px solid #e2e8ea}
.detail h5{font-size:7.5px;margin:8px 0 3px}
.detail p{color:#555}
.actionbar{flex:none;height:44px;background:var(--pink);display:flex;justify-content:center;align-items:center;gap:8px}
.actionbar .btn{background:var(--white);color:var(--pink);width:40px;height:28px;font-size:9px}

/* cv */
.cv-head{display:flex;gap:6px;padding:6px;position:relative;font-size:6.5px;line-height:1.35}
.avatar{width:38px;height:44px;flex:none;background:linear-gradient(180deg,#c9a792,#7d5d4d)}
.cv-row{display:flex;justify-content:space-between;align-items:center;padding:0 6px;height:21px;font-size:7.5px;font-weight:700;margin-bottom:4px}
.mini{background:var(--link);color:var(--white);font-size:6.5px;font-weight:700;border-radius:3px;width:26px;height:12px;display:flex;align-items:center;justify-content:center}

/* profile */
.inputs{display:flex;flex-direction:column;gap:6px}
.input{height:20px;background:var(--white);border:1px solid #9fd8e6;border-radius:3px;font-size:7px;color:var(--link);font-weight:600;padding:0 8px;display:flex;align-items:center}
.input.tall{height:40px;align-items:flex-start;padding-top:5px}
.save{width:90px;height:13px;margin:6px auto 0;font-size:8px}

/* skills */
.skill{display:flex;height:24px;margin-bottom:6px}
.skill span{flex:1;background:var(--white);border:1px solid #9fd8e6;border-right:0;font-size:7px;display:flex;align-items:center;padding-left:8px}
.skill b{width:22px;background:var(--link);color:var(--white);font-size:11px;font-weight:400;display:flex;align-items:center;justify-content:center}

/* settings */
.set-group{padding:6px 8px;margin-bottom:6px;font-size:7px}
.set-group h6{font-size:7.5px;font-weight:700;margin-bottom:4px}
.set-line{display:flex;justify-content:space-between;align-items:center;height:13px}
.toggle{width:18px;height:9px;border-radius:5px;background:#d5dadd;position:relative}
.toggle::after{content:"";position:absolute;right:1px;top:1px;width:7px;height:7px;border-radius:50%;background:var(--white)}
.sq{width:9px;height:9px;border-radius:2px;background:var(--fb)}
.logout{width:64px;height:12px;margin:6px auto 0;background:var(--link);color:var(--white);font-size:7px;font-weight:700;border-radius:3px;display:flex;align-items:center;justify-content:center}
</style>
</head>
<body>
<svg width="0" height="0" style="position:absolute" aria-hidden="true">
  <symbol id="i-home" viewBox="0 0 26 24"><path d="M3 12 13 3l10 9M6 10v11h14V10" fill="none" stroke="#ef5a9d" stroke-width="2.2"/><rect x="11" y="14" width="5" height="7" fill="none" stroke="#ef5a9d" stroke-width="2"/></symbol>
  <symbol id="i-search" viewBox="0 0 26 24"><circle cx="11" cy="10" r="7" fill="none" stroke="#ef5a9d" stroke-width="2.4"/><path d="M16 15l7 7" stroke="#ef5a9d" stroke-width="3"/></symbol>
  <symbol id="i-case" viewBox="0 0 26 24"><rect x="3" y="7" width="20" height="14" rx="1" fill="none" stroke="#ef5a9d" stroke-width="2.2"/><path d="M9 7V4h8v3M3 13h20" fill="none" stroke="#ef5a9d" stroke-width="2"/></symbol>
  <symbol id="i-doc" viewBox="0 0 26 24"><rect x="6" y="2" width="14" height="20" fill="none" stroke="#ef5a9d" stroke-width="2.2"/><path d="M9 7h8M9 11h8M9 15h8" stroke="#ef5a9d" stroke-width="1.6"/></symbol>
  <symbol id="i-sliders" viewBox="0 0 26 24"><path d="M7 3v18M13 3v18M19 3v18" stroke="#ef5a9d" stroke-width="2"/><rect x="4" y="13" width="6" height="4" fill="#ef5a9d"/><rect x="10" y="6" width="6" height="4" fill="#ef5a9d"/><rect x="16" y="15" width="6" height="4" fill="#ef5a9d"/></symbol>
</svg>

<main class="board">

  <!-- Login -->
  <section class="screen login-splash" style="left:54px;top:180px;width:220px;height:420px">
    <div class="status"><span>●●●●●</span><span>9:41 AM</span><span>100%</span></div>
    <div class="center">
      <div class="wordmark">Roamjobs</div>
      <div class="connecting">Connecting....</div>
    </div>
  </section>

  <section class="screen login-photo" style="left:304px;top:180px;width:220px;height:420px">
    <div class="status"><span>●●●●●</span><span>9:41 AM</span><span>100%</span></div>
    <div class="brandbar"><div class="wordmark">Roamjobs</div></div>
    <div class="photo" role="img" aria-label="Photo of a young woman relaxing with eyes closed" style="background:linear-gradient(160deg,#8aa4b4,#b58c7a 55%,#5c4a45)">
      <div class="overlay"><div class="caption">Relax we'll help you</div><div class="dots"><i class="on"></i><i></i><i></i></div><div class="fb-btn"><i></i>Login with Friendlane</div></div>
    </div>
  </section>

  <section class="screen login-photo" style="left:554px;top:180px;width:220px;height:420px">
    <div class="status"><span>●●●●●</span><span>9:41 AM</span><span>100%</span></div>
    <div class="brandbar"><div class="wordmark">Roamjobs</div></div>
    <div class="photo" role="img" aria-label="Photo of hands sketching app screens beside a phone" style="background:linear-gradient(160deg,#eee9e2,#d9cfc4 60%,#b7a99a)">
      <div class="overlay"><div class="dots"><i></i><i class="on"></i><i></i></div><div class="fb-btn"><i></i>Login with Friendlane</div></div>
    </div>
  </section>

  <section class="screen login-photo" style="left:804px;top:180px;width:220px;height:420px">
    <div class="status"><span>●●●●●</span><span>9:41 AM</span><span>100%</span></div>
    <div class="brandbar"><div class="wordmark">Roamjobs</div></div>
    <div class="photo" role="img" aria-label="Photo of a hiker with arms raised on a mountain top" style="background:linear-gradient(180deg,#c6d2da,#a9b6bd 45%,#7b6b52 75%,#4f4534)">
      <div class="overlay"><div class="dots"><i></i><i></i><i class="on"></i></div><div class="fb-btn"><i></i>Login with Friendlane</div></div>
    </div>
  </section>

  <!-- Search results -->
  <section class="screen" style="left:137px;top:755px;width:236px;height:412px">
    <div class="status"><span>●●●●●</span><span>9:41 AM</span><span>100%</span></div>
    <div class="appbar"><span class="back"></span>Search</div>
    <div class="body">
      <div class="card result"><span class="co-mark" style="background:#2a6fb5"></span><div><h4>Senior Product Designer</h4><p>Silverframe Pictures<br>Stockholm,Sweden</p></div><span class="ago">2 days ago</span></div>
      <div class="card result"><span class="co-mark" style="background:#d42a3a"></span><div><h4>Senior Product Designer</h4><p>Kumotek<br>Stockholm,Sweden</p></div><span class="ago">5 days ago</span></div>
      <div class="card result"><span class="co-mark" style="background:#2d6fc0"></span><div><h4>Produkt Designer</h4><p>Bavarin Motors<br>Stockholm,Sweden</p></div><span class="ago">10 hours ago</span></div>
      <div class="card result"><span class="co-mark" style="background:#e9b323"></span><div><h4>UX/UI Designer</h4><p>Searchloom<br>Stockholm,Sweden</p></div><span class="ago">12 hours ago</span></div>
      <div class="card result"><span class="co-mark" style="background:#1f7a4d"></span><div><h4>Senior Digital Designer</h4><p>Greenbean Cafe<br>Stockholm,Sweden</p></div><span class="ago">2 days ago</span></div>
    </div>
    <nav class="tabbar"><span class="tab"><svg><use href="#i-home"/></svg></span><span class="tab"><svg><use href="#i-search"/></svg></span><span class="tab"><svg><use href="#i-case"/></svg></span><span class="tab"><svg><use href="#i-doc"/></svg></span><span class="tab"><svg><use href="#i-sliders"/></svg></span></nav>
  </section>

  <!-- Search -->
  <section class="screen" style="left:419px;top:735px;width:236px;height:438px">
    <div class="status"><span>●●●●●</span><span>9:41 AM</span><span>100%</span></div>
    <div class="appbar">Search</div>
    <div class="body">
      <div class="search-form">
        <div class="field">Job title, Keyword, Company<span class="drop"></span></div>
        <div class="field">Country<span class="drop"></span></div>
        <div class="field">Location<span class="drop"></span></div>
      </div>
      <div class="search-go">Search job</div>
    </div>
    <nav class="tabbar"><span class="tab"><svg><use href="#i-home"/></svg></span><span class="tab"><svg><use href="#i-search"/></svg></span><span class="tab"><svg><use href="#i-case"/></svg></span><span class="tab"><svg><use href="#i-doc"/></svg></span><span class="tab"><svg><use href="#i-sliders"/></svg></span></nav>
  </section>

  <!-- Job details -->
  <section class="screen" style="left:685px;top:755px;width:236px;height:412px">
    <div class="status"><span>●●●●●</span><span>9:41 AM</span><span>100%</span></div>
    <div class="appbar"><span class="close">✕</span>Job Details</div>
    <div class="body">
      <div class="card detail">
        <div class="head"><span class="co-mark" style="background:#2a6fb5"></span><div><b style="font-size:7.5px">Senior Product Designer</b><br><span style="color:#7b8790">Silverframe Pictures<br>Stockholm,Sweden</span></div><span style="position:absolute;right:0;top:0;color:#7b8790">2 days ago</span></div>
        <h5>Job Description</h5>
        <p>We are looking for a curious designer to shape playful mobile experiences. You will work closely with product and engineering, turn research into clear flows, build prototypes, test ideas with real users and keep our visual language fresh, friendly and simple across every screen we ship.</p>
        <h5>Skills</h5>
        <p>Strong portfolio of mobile work, fluent in modern design tools, good sense of type and colour, able to explain choices, comfortable with quick feedback loops and happy working in a small team.</p>
      </div>
    </div>
    <div class="actionbar"><span class="btn">Skip</span><span class="btn">Save</span><span class="btn">Apply</span></div>
  </section>

  <!-- My CV -->
  <section class="screen" style="left:38px;top:1461px;width:234px;height:490px">
    <div class="status"><span>●●●●●</span><span>9:41 AM</span><span>100%</span></div>
    <div class="appbar">My CV</div>
    <div class="body" style="padding:4px 6px">
      <div class="card cv-head"><div class="avatar" role="img" aria-label="Profile portrait"></div><div><b style="font-size:7.5px">Elin Varga</b><br>Interface Designer<br>Stockholm, Sweden<br>elin@mail.se</div><span class="mini" style="position:absolute;right:6px;top:14px">Edit</span></div>
      <div style="font-size:6.5px;color:#555;padding:3px 2px">Creative interface designer who loves clean flows</div>
      <div class="card" style="padding:4px 6px;margin-bottom:4px;font-size:6.5px;line-height:1.4;position:relative">
        <b style="font-size:7.5px">Work Experience</b><span class="mini" style="position:absolute;right:6px;top:4px">Add</span><br>
        <span style="color:#d42a3a;font-weight:700">Nordhaus</span>&nbsp; Interface Designer<span class="mini" style="position:absolute;right:6px;top:20px">Edit</span><br>April 2013 to Present (about 4 years)
      </div>
      <div class="card cv-row">Education<span class="mini">Add</span></div>
      <div class="card cv-row">Links<span class="mini">Add</span></div>
      <div class="card cv-row">Skills<span class="mini">Add</span></div>
      <div class="card cv-row">Awards<span class="mini">Add</span></div>
      <div class="card cv-row">Certifications/Licenses<span class="mini">Add</span></div>
      <div class="card cv-row">Group<span class="mini">Add</span></div>
      <div class="card cv-row">Patents<span class="mini">Add</span></div>
      <div class="card cv-row">Publications<span class="mini">Add</span></div>
    </div>
    <nav class="tabbar"><span class="tab"><svg><use href="#i-home"/></svg></span><span class="tab"><svg><use href="#i-search"/></svg></span><span class="tab"><svg><use href="#i-case"/></svg></span><span class="tab"><svg><use href="#i-doc"/></svg></span><span class="tab"><svg><use href="#i-sliders"/></svg></span></nav>
  </section>

  <!-- Profile -->
  <section class="screen" style="left:296px;top:1461px;width:234px;height:490px">
    <div class="status"><span>●●●●●</span><span>9:41 AM</span><span>100%</span></div>
    <div class="appbar"><span class="back"></span>Profile</div>
    <div class="body">
      <div class="inputs">
        <div class="input">First Name</div><div class="input">Last Name</div><div class="input">Email</div>
        <div class="input">Gender</div><div class="input">Birthday</div><div class="input">City</div>
        <div class="input">State</div><div class="input">Country</div>
        <div class="input">Write a location about me</div>
        <div class="input tall">Summary</div>
      </div>
      <div class="btn save" style="display:flex">Save</div>
    </div>
    <nav class="tabbar"><span class="tab"><svg><use href="#i-home"/></svg></span><span class="tab"><svg><use href="#i-search"/></svg></span><span class="tab"><svg><use href="#i-case"/></svg></span><span class="tab"><svg><use href="#i-doc"/></svg></span><span class="tab"><svg><use href="#i-sliders"/></svg></span></nav>
  </section>

  <!-- Skills -->
  <section class="screen" style="left:552px;top:1461px;width:232px;height:490px">
    <div class="status"><span>●●●●●</span><span>9:41 AM</span><span>100%</span></div>
    <div class="appbar"><span class="back"></span>Skills</div>
    <div class="body">
      <div class="btn" style="display:flex;width:150px;height:22px;margin:4px auto 14px;background:#fff;color:var(--link);border:1px solid #9fd8e6">Add</div>
      <div class="skill"><span>Digital Design</span><b>✕</b></div>
      <div class="skill"><span>Business Development</span><b>✕</b></div>
      <div class="skill"><span>App Design</span><b>✕</b></div>
      <div class="btn save" style="display:flex;background:var(--link);margin-top:12px">Save</div>
    </div>
    <nav class="tabbar"><span class="tab"><svg><use href="#i-home"/></svg></span><span class="tab"><svg><use href="#i-search"/></svg></span><span class="tab"><svg><use href="#i-case"/></svg></span><span class="tab"><svg><use href="#i-doc"/></svg></span><span class="tab"><svg><use href="#i-sliders"/></svg></span></nav>
  </section>

  <!-- Settings -->
  <section class="screen" style="left:809px;top:1461px;width:231px;height:490px">
    <div class="status"><span>●●●●●</span><span>9:41 AM</span><span>100%</span></div>
    <div class="appbar">Settings</div>
    <div class="body">
      <div class="card set-group"><h6>Notifications</h6>
        <div class="set-line">Job Messages<span class="toggle"></span></div>
        <div class="set-line">Send notification by Email too<span class="toggle"></span></div>
      </div>
      <div class="card set-group">
        <div class="set-line">Like us on<span class="sq"></span></div>
        <div class="set-line">Share on<span class="sq" style="background:#1f8fd6"></span></div>
        <div class="set-line">Follow us<span class="sq" style="background:#3fb0e8"></span></div>
        <div class="set-line">Rate us on<span class="sq" style="background:#e3453a"></span></div>
      </div>
      <div class="card set-group"><h6>Help</h6>
        <div class="set-line">Privacy Policy</div>
        <div class="set-line">Terms of Use</div>
      </div>
      <div class="card set-group"><div class="set-line">Version 1.0</div></div>
      <div class="logout">Logout</div>
    </div>
    <nav class="tabbar"><span class="tab"><svg><use href="#i-home"/></svg></span><span class="tab"><svg><use href="#i-search"/></svg></span><span class="tab"><svg><use href="#i-case"/></svg></span><span class="tab"><svg><use href="#i-doc"/></svg></span><span class="tab"><svg><use href="#i-sliders"/></svg></span></nav>
  </section>

</main>
</body>
</html>
```